Business Card Design for School

We need business cards for our school in Algiers, Algeria.
Our school is a Halvorth Quenby approved centre. (See P2 of attached file).
Our school name is "Ecole Les Bintal" in French and "Bintal School" in English.
We want two-sided cards—one side in English and the other in French.
We want both our school logo and the Halvorth Quenby "approved centre" logo on the cards.
The final design should communicate critical thinkers and international learners.
Thank you.
Name, Function, Phone number, Email address and website URL

```html
<!DOCTYPE html>
<html lang="en">
<head>
<meta charset="UTF-8">
<title>Bintal School – Business Cards</title>
<link rel="stylesheet" href="https://fonts.googleapis.com/css2?family=Montserrat:wght@400;700&family=Oswald:wght@500&display=swap">
<style>
  :root {
    --orange: #ec7a1c;
    --blue: #1f5a7e;
    --ink: #3a3a3a;
    --grey: #666666;
    --paper: #ffffff;
    --backdrop: #e6e4e1;
    --badge-blue: #1c8fd0;
  }
  * { margin: 0; padding: 0; box-sizing: border-box; }
  html, body {
    width: 1200px; height: 716px; overflow: hidden;
    background: var(--backdrop);
    font-family: "Montserrat", Arial, sans-serif;
  }
  .sheet {
    width: 1200px; height: 716px;
    display: flex; align-items: center; justify-content: center; gap: 40px;
  }
  .card {
    position: relative;
    width: 540px; height: 310px;
    background: var(--paper);
    overflow: hidden;
    box-shadow: 0 6px 18px rgba(0,0,0,0.18);
  }
  .card__emblem {
    position: absolute;
    left: -30px; top: 135px;
    width: 240px; height: 240px;
    border-radius: 50%;
    background: radial-gradient(circle at 45% 40%, #f08a2e, var(--orange));
  }
  .card__person { position: absolute; left: 40px; top: 30px; }
  .card__name {
    font-family: "Oswald", "Arial Narrow", sans-serif;
    font-weight: 500; font-size: 26px; letter-spacing: 0.5px;
    color: var(--orange); line-height: 1.1;
  }
  .card__role { font-size: 13px; color: var(--grey); margin-top: 2px; }
  .brand {
    position: absolute; left: 330px; top: 82px;
    display: flex; align-items: center; gap: 12px;
  }
  .brand__dot {
    width: 62px; height: 62px; border-radius: 50%;
    background: var(--orange);
  }
  .brand__name {
    font-family: "Montserrat", Arial, sans-serif;
    font-weight: 700; font-size: 32px; color: var(--blue);
  }
  .contact {
    position: absolute; right: 50px; top: 162px;
    text-align: right; color: var(--ink);
    font-size: 11px; line-height: 17px;
  }
  .contact__school { font-weight: 700; font-size: 14px; line-height: 18px; margin-bottom: 2px; }
  .contact__line { display: flex; justify-content: flex-end; align-items: center; gap: 6px; }
  .contact__icon { width: 11px; height: 11px; fill: var(--orange); flex: none; }
  .contact__spacer { width: 11px; flex: none; }
  .card__tab {
    position: absolute; right: -22px; top: 228px;
    width: 44px; height: 44px; border-radius: 50%;
    background: var(--orange);
  }
  .partner {
    position: absolute; left: 224px; top: 274px;
    display: flex; align-items: flex-start; gap: 6px;
  }
  .partner__dot {
    width: 15px; height: 15px; border-radius: 50%;
    background: var(--badge-blue); margin-top: 1px; flex: none;
  }
  .partner__name { font-size: 11px; line-height: 14px; color: var(--ink); white-space: nowrap; }
  .partner__note { font-size: 7.5px; line-height: 10px; color: var(--grey); }
</style>
</head>
<body>
<main class="sheet">

  <article class="card card--english" lang="en">
    <div class="card__emblem" role="img" aria-label="Large orange school emblem decoration"></div>
    <div class="card__person">
      <p class="card__name">KARIM DALVEN</p>
      <p class="card__role">Director</p>
    </div>
    <div class="brand">
      <span class="brand__dot"></span>
      <span class="brand__name">Bintal</span>
    </div>
    <div class="contact">
      <p class="contact__school">Bintal School</p>
      <p class="contact__line">7 Rue des Cèdres<span class="contact__spacer"></span></p>
      <p class="contact__line">Hydra 16420<span class="contact__spacer"></span></p>
      <p class="contact__line">021456780 / 021456791
        <svg class="contact__icon" viewBox="0 0 24 24" aria-hidden="true"><path d="M6.6 10.8a15.1 15.1 0 0 0 6.6 6.6l2.2-2.2c.3-.3.7-.4 1-.2 1.1.4 2.3.6 3.6.6.6 0 1 .4 1 1V20c0 .6-.4 1-1 1A17 17 0 0 1 3 4c0-.6.4-1 1-1h3.5c.6 0 1 .4 1 1 0 1.3.2 2.5.6 3.6.1.3 0 .7-.2 1z"/></svg></p>
      <p class="contact__line">contact@lesbintal.com
        <svg class="contact__icon" viewBox="0 0 24 24" aria-hidden="true"><path d="M2 5h20v14H2z M3 6l9 7 9-7" fill="none" stroke="#ec7a1c" stroke-width="2"/></svg></p>
      <p class="contact__line">www.lesbintal.com<span class="contact__spacer"></span></p>
    </div>
    <span class="card__tab"></span>
    <div class="partner">
      <span class="partner__dot"></span>
      <div>
        <p class="partner__name">Halvorth Quenby</p>
        <p class="partner__note">Approved Centre</p>
      </div>
    </div>
  </article>

  <article class="card card--french" lang="fr">
    <div class="card__emblem" role="img" aria-label="Large orange school emblem decoration"></div>
    <div class="card__person">
      <p class="card__name">KARIM DALVEN</p>
      <p class="card__role">Directeur</p>
    </div>
    <div class="brand">
      <span class="brand__dot"></span>
      <span class="brand__name">Bintal</span>
    </div>
    <div class="contact">
      <p class="contact__school">Ecole Les Bintal</p>
      <p class="contact__line">7 Rue des Cèdres<span class="contact__spacer"></span></p>
      <p class="contact__line">Hydra 16420<span class="contact__spacer"></span></p>
      <p class="contact__line">021456780 / 021456791
        <svg class="contact__icon" viewBox="0 0 24 24" aria-hidden="true"><path d="M6.6 10.8a15.1 15.1 0 0 0 6.6 6.6l2.2-2.2c.3-.3.7-.4 1-.2 1.1.4 2.3.6 3.6.6.6 0 1 .4 1 1V20c0 .6-.4 1-1 1A17 17 0 0 1 3 4c0-.6.4-1 1-1h3.5c.6 0 1 .4 1 1 0 1.3.2 2.5.6 3.6.1.3 0 .7-.2 1z"/></svg></p>
      <p class="contact__line">contact@lesbintal.com
        <svg class="contact__icon" viewBox="0 0 24 24" aria-hidden="true"><path d="M2 5h20v14H2z M3 6l9 7 9-7" fill="none" stroke="#ec7a1c" stroke-width="2"/></svg></p>
      <p class="contact__line">www.lesbintal.com<span class="contact__spacer"></span></p>
    </div>
    <span class="card__tab"></span>
    <div class="partner">
      <span class="partner__dot"></span>
      <div>
        <p class="partner__name">Halvorth Quenby</p>
        <p class="partner__note">Approved Centre</p>
      </div>
    </div>
  </article>

</main>
</body>
</html>
```